The Gentle Moonlit Harbour Journey

This book accompanies a video workshop. The book explains who our guardian angels are, what is their purpose, how to connect with them for wisdom & guidance. How to manifest what we world like bring into our lives by asking the Angels. The book contains meditation exercises, lots of information and fun facts about how our angels give us messages and guidance and how to become more intuitive. How to use angel oracle cards to receive guidance from our angels.
I'm quite an upbeat, happy person, so the book is written very warmly and is a collection of all the information that out ther, drawn together neatly by me, with my own unique take on all things angelic. Along with personal stories and anecdotes about how and why I became interested in angels and what they have taught me. It's fun, fresh, lighthearted and modern. Not at all serious, just extremely uplifting and positive, so I would really like the cover to reflect this.

Target Market(s)

Anyone who is interested in angels. From my chatterloop page activity I find it is mostly women of all ages who are interested in angels

Font styles to use
Serif
Sans Serif
Script

Colors
ea8dbb
f04a50
e667a6
e34197
85abd2
886aae
b7a5cd
6b449b
fbee3e

Requirements
Must have
• A more feminine appeal
• Look quite modern & upbeat but also calming and open
• I would like it to look etherel in some way. I definitely dont want something that looks like a cartoon or clip art
Should not have
• No dark colours or sinister imagery. I don't want people to feel like thus can't do the & it's only special people who can connect with their angels
• No haunting imagery!

```html
<!DOCTYPE html>
<html lang="en">
<head>
<meta charset="utf-8">
<title>The Gentle Moonlit Harbour Journey – Book Cover</title>
<link rel="stylesheet" href="https://fonts.googleapis.com/css2?family=Great+Vibes&family=Gelasio:ital,wght@0,400;1,400&display=swap">
<style>
  :root {
    --page-bg: #eef1f3;
    --sky-top: #8ec4ea;
    --sky-mid: #c4e2f3;
    --sky-low: #eaf5fa;
    --cloud-white: #ffffff;
    --wing-white: #fbfcfe;
    --wing-shadow: #d3e1ec;
    --ink-soft: #5b6470;
    --title-purple: #8a4fe0;
    --title-teal: #5fe6c6;
    --title-lilac: #b76ee8;
    --author-grey: #6b6f76;
  }
  * { margin: 0; padding: 0; box-sizing: border-box; }
  html, body {
    width: 1000px; height: 1200px; overflow: hidden;
    background: var(--page-bg);
  }
  .book-cover {
    position: absolute; left: 131px; top: 50px;
    width: 737px; height: 1100px; overflow: hidden;
    background: linear-gradient(180deg, var(--sky-top) 0%, var(--sky-mid) 40%, var(--sky-low) 70%, var(--cloud-white) 100%);
    box-shadow: 0 10px 30px rgba(60, 80, 100, 0.18);
  }
  .cloud-bank {
    position: absolute; left: 0; right: 0; bottom: 0; height: 520px;
    background:
      radial-gradient(ellipse 60% 35% at 25% 45%, rgba(255,255,255,0.95), rgba(255,255,255,0) 70%),
      radial-gradient(ellipse 55% 30% at 75% 60%, rgba(255,255,255,0.95), rgba(255,255,255,0) 70%),
      linear-gradient(180deg, rgba(255,255,255,0) 0%, var(--cloud-white) 75%);
  }
  .angel-wing {
    position: absolute; left: 80px; top: 200px; width: 700px; height: 520px;
    border-radius: 60% 40% 30% 50% / 55% 45% 50% 50%;
    background: radial-gradient(ellipse 70% 60% at 60% 35%, var(--wing-white) 0%, rgba(251,252,254,0.9) 45%, rgba(211,225,236,0.6) 70%, rgba(211,225,236,0) 100%);
    transform: rotate(-8deg);
  }
  .tagline {
    position: absolute; top: 76px; left: 0; right: 0;
    text-align: center;
    font-family: "Gelasio", Georgia, serif; font-style: italic; font-weight: 400;
    font-size: 19px; line-height: 1.35; color: var(--ink-soft);
  }
  .title-block {
    position: absolute; top: 372px; left: 0; right: 0;
    text-align: center; font-weight: 400;
  }
  .title-lead {
    display: block; padding-left: 150px;
    font-family: "Gelasio", Georgia, serif; font-weight: 400;
    font-size: 30px; line-height: 1; color: var(--title-teal);
  }
  .title-main {
    display: block; margin-top: 4px;
    font-family: "Great Vibes", cursive; font-weight: 400;
    font-size: 150px; line-height: 1.05; color: var(--title-purple);
  }
  .title-second {
    display: block; margin-top: 2px;
    font-family: "Gelasio", Georgia, serif; font-weight: 400;
    font-size: 66px; line-height: 1; color: var(--title-teal);
  }
  .title-third {
    display: block; margin-top: 8px;
    font-family: "Gelasio", Georgia, serif; font-weight: 400;
    font-size: 40px; line-height: 1; color: var(--title-lilac);
  }
  .author-name {
    position: absolute; top: 945px; left: 0; right: 0;
    text-align: center;
    font-family: "Gelasio", Georgia, serif; font-weight: 400;
    font-size: 30px; color: var(--author-grey);
  }
</style>
</head>
<body>
  <main class="book-cover">
    <div class="cloud-bank" role="img" aria-label="Soft white clouds drifting across a pale sky"></div>
    <div class="angel-wing" role="img" aria-label="Large feathered white angel wing spreading across the sky"></div>
    <p class="tagline">Connect with your angels<br>bring love, healing and divine guidance<br>to every area of your life</p>
    <h1 class="title-block">
      <span class="title-lead">the gentle</span>
      <span class="title-main">Moonlit</span>
      <span class="title-second">Harbour</span>
      <span class="title-third">Journey</span>
    </h1>
    <p class="author-name">Rosalind Avery</p>
  </main>
</body>
</html>
```